Plumbing Website

Design a simple 4 page website based on our provided logo and sketches. Winning designer should be willing to upgrade as needed (for additional fee). A design that includes SEO features is a plus.
I would like to see Home, , Services, Recent Jobs (set up for pictures), Contact. I like the water dropplet back ground. Please dont put logo in a box. File attached as exaple only, I am looking for a request service now button in the middle that will have a form fill to be emailed to two different addresses,
I would like to see vibrant colors. Examples of sites I like are www.brightvalvepipeworks.com look also at www.kmt-keystonemeridianpipes.com - this site is too busy but has good seo features.
Industry/Entity Type
Plumbing
Look and feel

```html
<!DOCTYPE html>
<html lang="en">
<head>
<meta charset="utf-8">
<title>Sierra Crest Plumbing</title>
<link href="https://fonts.googleapis.com/css2?family=Carlito:wght@400;700&family=Pathway+Gothic+One&display=swap" rel="stylesheet">
<style>
:root{
  --red:#c1121f;
  --red-dark:#9d0e18;
  --beige:#e2ddd4;
  --ink:#222;
  --text:#2b2b2b;
  --blue:#1463b8;
  --water-light:#bfe3f7;
  --water-mid:#5ab2e6;
  --water-deep:#2f86cc;
  --dark:#1f1f1f;
  --muted:#9a9a9a;
  --white:#fff;
}
*{margin:0;padding:0;box-sizing:border-box}
html,body{width:984px;height:1200px;overflow:hidden}
body{position:relative;background:var(--beige);font-family:"Carlito",Calibri,sans-serif;color:var(--text)}
.abs{position:absolute}
.display{font-family:"Pathway Gothic One","Oswald",sans-serif;font-weight:400}
.topbar{left:0;top:0;width:984px;height:48px;background:var(--beige)}
.redband{left:0;top:48px;width:984px;height:82px;background:linear-gradient(var(--red),var(--red-dark))}
.water{left:0;top:130px;width:984px;height:1008px;background:radial-gradient(circle at 30% 20%,var(--water-light),transparent 40%),radial-gradient(circle at 80% 70%,var(--water-light),transparent 45%),linear-gradient(180deg,var(--water-mid),var(--water-deep) 50%,var(--water-mid))}
.logo-plate{left:50px;top:0;width:212px;height:150px}
.logo-name{left:50px;top:40px;width:212px;text-align:center;color:var(--blue);font-weight:700;font-size:22px;line-height:26px;letter-spacing:1px}
.social{top:9px;display:flex;gap:6px;left:282px}
.social span{width:28px;height:28px;border-radius:50%;background:#a9a6a1;display:block}
.callnum{right:49px;top:10px;font-size:27px;color:var(--ink)}
.callnum b{font-weight:400;color:var(--blue)}
.nav{top:73px;left:280px;display:flex;align-items:center;height:34px}
.nav a{color:var(--white);text-decoration:none;font-size:25px;line-height:34px}
.nav .sep{width:0;height:40px;border-left:3px dotted var(--white);margin:0 22px}
.emergency{left:741px;top:71px;width:194px;height:39px;background:linear-gradient(#fff,#e6e6e6);border-radius:3px;color:var(--blue);font-size:24px;text-align:center;line-height:39px}
.panel{background:var(--white);box-shadow:0 0 6px rgba(0,0,0,.25)}
.intro{left:49px;top:173px;width:517px;height:319px}
.intro h1{position:absolute;left:0;top:18px;width:100%;text-align:center;font-size:24px;color:var(--ink);font-weight:400}
.intro h1 em{font-style:normal;color:var(--red)}
.intro .rule{position:absolute;left:0;top:62px;width:100%;height:8px;background:linear-gradient(#eee,#fff)}
.intro .copy{position:absolute;left:25px;top:88px;width:467px;font-size:13.4px;line-height:17.9px;text-align:justify}
.intro .copy p{margin-bottom:17.9px}
.photo{background:linear-gradient(135deg,#8a3a22,#2c2420 45%,#d7d3cf 80%,#9aa3ad)}
.hero{left:584px;top:173px;width:351px;height:319px}
.services{left:49px;top:516px;width:886px;height:441px}
h2.sec{position:absolute;font-size:24px;color:var(--red);font-weight:400;line-height:28px}
.thumb{position:absolute;border:3px solid var(--blue)}
.svc{position:absolute;font-size:13.4px;line-height:16.2px;text-align:justify}
.divider{position:absolute;left:60px;top:251px;width:766px;height:2px;background:linear-gradient(90deg,transparent,#ddd,transparent)}
.contact{left:49px;top:984px;width:886px;height:139px;background:var(--dark);border-top:3px solid var(--red)}
.contact .lbl{position:absolute;color:var(--muted);font-size:17px}
.contact .phone{position:absolute;left:34px;top:58px;font-size:42px;color:var(--white);line-height:44px}
.contact .email{position:absolute;left:282px;top:62px;font-size:21px;color:var(--white)}
.contact .vsep{position:absolute;top:36px;height:64px;border-left:5px dotted #888}
.contact .btn{position:absolute;left:707px;top:43px;width:143px;height:40px;background:var(--red);border:1px solid #e04a52;color:var(--white);font-size:23px;text-align:center;line-height:38px}
.footer{left:50px;top:1154px;font-size:10px;line-height:16px;color:var(--ink)}
.share{right:49px;top:1161px;display:flex;gap:4px;font-size:10px}
.share span{border:1px solid #bbb;background:#f4f4f4;padding:0 4px;line-height:15px}
</style>
</head>
<body>
<div class="abs topbar"></div>
<div class="abs redband"></div>
<div class="abs water" role="img" aria-label="Background of water droplets on blue glass"></div>

<svg class="abs logo-plate" viewBox="0 0 212 150" aria-hidden="true">
  <path d="M0 0H212V128L106 150L0 128Z" fill="#f3f3f3" stroke="#cfcfcf"/>
</svg>
<div class="abs logo-name">SIERRA CREST<br>PLUMBING</div>

<div class="abs social" aria-label="Social links"><span></span><span></span><span></span><span></span></div>
<div class="abs callnum display">CALL: <b>555-014-2290</b></div>

<nav class="abs nav display">
  <a href="#">HOME</a><span class="sep"></span>
  <a href="#">SERVICES</a><span class="sep"></span>
  <a href="#">RECENT JOBS</a><span class="sep"></span>
  <a href="#">CONTACT US</a>
</nav>
<div class="abs emergency display">PLUMBING EMERGENCY</div>

<section class="abs panel intro">
  <h1 class="display">FOR IMMEDIATE SERVICE, CALL <em>555-014-2290</em></h1>
  <div class="rule"></div>
  <div class="copy">
    <p>Sierra Crest Plumbing is the industry leader in the area.&nbsp; We are a Plumbing, Drain Cleaning, and General Engineering contractors, providing excellent customer service and helping homeowners to live more comfortable and healthy lives.</p>
    <p>If you are looking for a Plumber in Cedar Valley then call on Sierra Crest Plumbing as your Plumbing Contractor.</p>
    <p>When the water heater bursts or the bathroom is flooding, do you want the best plumber available, or do you want the cheapest?&nbsp; At Sierra Crest Plumbing, we know that the best plumber does world-class work, is fully licensed and insured, is available 24/7 – including during emergencies – and somehow combines world-class equipment and service with world-class affordability.</p>
  </div>
</section>
<div class="abs photo hero" role="img" aria-label="Photo of a plumber's hands fitting pipes under a sink"></div>

<section class="abs panel services">
  <h2 class="sec display" style="left:26px;top:37px">PLUMBING</h2>
  <div class="thumb photo" style="left:27px;top:64px;width:188px;height:153px;background:linear-gradient(135deg,#dfe6ee,#9fb2c6 50%,#c45a3a)" role="img" aria-label="Photo of a hand tightening a chrome pipe with a red wrench"></div>
  <p class="svc" style="left:228px;top:61px;width:202px">We are a full-service plumbing company.&nbsp; Our plumbers are experts at repairing or replacing all types of leaks, faucets, toilets, water heaters, drain and sewer pipes, water lines, gas lines/earthquake valves, garbage disposers, and re-circulating pumps.</p>

  <h2 class="sec display" style="left:455px;top:37px">DRAIN CLEANING</h2>
  <div class="thumb photo" style="left:456px;top:64px;width:188px;height:153px;background:linear-gradient(160deg,#6f8a4a,#9bbf3a 45%,#5e6060)" role="img" aria-label="Photo of a worker in hi-vis gear cleaning a street drain"></div>
  <p class="svc" style="left:658px;top:61px;width:201px">We have been cleaning drains for almost 20 years.&nbsp; Whether it's a kitchen sink or a main sewer line stoppage, we have cleaned them all!&nbsp; We are equipped with some of the newest technology available from color sewer camera's with electronic line locator's and trench-less sewer repairs, we stay up to date to save you money!</p>

  <div class="divider"></div>

  <h2 class="sec display" style="left:26px;top:288px">GENERAL ENGINEERING</h2>
  <div class="thumb photo" style="left:27px;top:316px;width:188px;height:98px;background:linear-gradient(120deg,#5d6a78,#b9c9d8 50%,#7d8fa1)" role="img" aria-label="Photo of large industrial pipes"></div>
  <p class="svc" style="left:228px;top:313px;width:640px;line-height:17.9px">What sets us apart, is being a class “A” engineering contractor.&nbsp; On larger projects that require cutting concrete and asphalt, excavating, repairing larger pipe, or entering into the city right of way- We CAN handle it.&nbsp; Other contractors must sub-contract work like this,&nbsp; we do it all in-house. On commercial properties, we learn every aspect of the domestic water, fire water, irrigation supply, sewer and storm drain system, when something fails, we already know where everything is and how to solve the problem quickly.&nbsp; In addition to normal plumbing products, we keep 4, 6 and 8” water fittings.&nbsp; After hour emergencies are handled with ease.</p>
</section>

<section class="abs contact">
  <div class="lbl" style="left:34px;top:36px">You can reach us at</div>
  <div class="phone display">555-014-2290</div>
  <div class="vsep" style="left:233px"></div>
  <div class="lbl" style="left:282px;top:44px">You can also contact us at our e-mail address:</div>
  <div class="email">service@sierracrestplumbing.com</div>
  <div class="vsep" style="left:657px"></div>
  <div class="btn display">CONTACT US</div>
</section>

<footer class="abs footer">
  © Sierra Crest Plumbing, 2013 - SCP Sierra Crest Plumbing LIC #480213<br>
  Home : Services : Recent Jobs | Contact Us
</footer>
<div class="abs share"><span>Like</span><span>8.6k</span><span>Share</span><span>831</span></div>
</body>
</html>
```